Medical Advertising Website Design
website redesign
Medical Advertising Website Design - Advertising
Creative Brief
Advertising
http://www.kvmedlink.example/
K&V medlink is an ad agency with 100% focus on healthcare (pharmaceutical company) clients. Here is copy for the open web page which gives an overview--
K&V MEDLINK COMMUNICATIONS
YOUR STRATEGIC PARTNER
[GLOBAL HEADLINE]
Raising Strategic Partnership to a Higher Level
TABS
Who We Are
Our Approach
What We Do
Therapeutic Experience
Our Work
Contact Us
At K&V our clients are our partners. We believe that being a great partner means going beyond the expected to bring value through the superior customer experience.
• Strong Key Opinion Leader relationships
• Specialized in “high science” markets
• Industry side experience… “We’ve sat in your chair”
• Superior program financial management
• A leader in managing today’s increased compliance requirements
[Subhead]
Our Mission
“Our customer service mission is to develop superior client relationships built on a mutual trust and a strategic partnership. This partnership is built through our superior industry knowledge, clear understanding of client objectives and expectations, and from the extraordinary value K&V provides beyond the programs we deliver. Our excellence is defined by unwavering quality of work, attention to detail, consistent/timely communications, flexibility to change, and through fair and reasonable pricing. Ultimately, it is our commitment to these values that result in anticipating and exceeding our clients expectations.”
Likes - unique yet professional, clean, crisp design Dislikes - bland, boring appearance. Clutter. Lack of flow. No Flash as iPads / iPhones can't read them.
Service Oriented
PMS 301
bright greens like PMS 362
maybe orange/yellow oranges for emphasis
below header
Company emphasis is strategic partnership for all of their clients

```html
<!DOCTYPE html>
<html lang="en">
<head>
<meta charset="utf-8">
<title>K&amp;V Medlink Communications</title>
<link href="https://fonts.googleapis.com/css2?family=Arimo:wght@400;700&display=swap" rel="stylesheet">
<style>
  :root {
    --brand-blue: #1d6fc0;
    --link-blue: #2a6fb8;
    --ink: #2b2b2b;
    --body-grey: #4a4a4a;
    --muted: #6b6b6b;
    --rule: #c9c9c9;
    --paper: #ffffff;
    --photo-dark: #0e0e0e;
    --photo-mid: #5a5d60;
    --photo-light: #c4c7c9;
  }
  * { box-sizing: border-box; margin: 0; padding: 0; }
  html, body { width: 1200px; height: 961px; overflow: hidden; background: var(--paper); }
  body { font-family: "Arimo", Arial, sans-serif; color: var(--body-grey); position: relative; }

  .hero {
    position: absolute; left: 0; top: 0; width: 1200px; height: 362px;
    background: linear-gradient(90deg, var(--photo-dark) 0%, #1c1d1f 22%, var(--photo-mid) 45%, var(--photo-light) 62%, #8e9295 78%, #3c3e40 100%);
  }
  .main-nav { position: absolute; right: 832px; top: 44px; text-align: right; }
  .main-nav a {
    display: block; font-weight: 700; font-size: 33px; line-height: 45px;
    color: #fff; text-decoration: none; letter-spacing: -0.5px;
  }
  .main-nav a::after { content: "\2022"; font-size: 14px; margin-left: 5px; vertical-align: middle; }
  .main-nav a.is-current { color: var(--brand-blue); }

  .brand { position: absolute; left: 148px; top: 424px; display: flex; align-items: center; gap: 10px; }
  .brand-mark { width: 46px; height: 46px; background: var(--brand-blue); }
  .brand-name { font-size: 13px; font-weight: 700; color: var(--brand-blue); line-height: 16px; width: 150px; }

  .headline {
    position: absolute; left: 396px; top: 426px;
    font-size: 31px; font-weight: 400; color: var(--brand-blue); letter-spacing: -0.5px;
  }
  .column { position: absolute; top: 478px; width: 320px; font-size: 13px; line-height: 17.5px; }
  .column h2 { font-size: 13px; font-weight: 700; color: var(--ink); margin-bottom: 2px; }
  .column ul { list-style: none; }
  .column li::before { content: "\2022 "; }
  .col-about { left: 396px; }
  .col-mission { left: 734px; width: 330px; }

  .news { position: absolute; left: 396px; top: 745px; font-size: 13px; line-height: 17.5px; }
  .news h2 { font-size: 13px; font-weight: 700; color: var(--ink); margin-bottom: 4px; }
  .news li { list-style: none; display: flex; }
  .news time { width: 86px; color: var(--muted); }
  .news a { color: var(--link-blue); text-decoration: none; }

  .site-footer {
    position: absolute; left: 148px; top: 905px; width: 920px;
    border-top: 1px solid var(--rule); padding-top: 10px;
    font-size: 12px; line-height: 17px; color: var(--ink);
  }
  .site-footer small { font-size: 11px; color: var(--muted); }
  .site-footer a { color: var(--link-blue); text-decoration: none; }
</style>
</head>
<body>
  <header class="hero" role="img" aria-label="Black and white photograph looking up at city skyscrapers"></header>

  <nav class="main-nav">
    <a class="is-current" href="#">Who We Are</a>
    <a href="#">Our Approach</a>
    <a href="#">What We Do</a>
    <a href="#">Experience</a>
    <a href="#">Our Work</a>
    <a href="#">Contact Us</a>
  </nav>

  <div class="brand">
    <span class="brand-mark"></span>
    <span class="brand-name">K&amp;V MEDLINK COMMUNICATIONS</span>
  </div>

  <h1 class="headline">Raising Strategic Partnership to a Higher Level</h1>

  <section class="column col-about">
    <h2>At K&amp;V</h2>
    <p>our clients are our partners. We believe that being a great partner means going beyond the expected to bring value through the superior customer experience.</p>
    <ul>
      <li>Strong Key Opinion Leader relationships</li>
      <li>Specialized in “high science” markets</li>
      <li>Industry side experience… “We’ve sat in your chair”</li>
      <li>Superior program financial management</li>
      <li>A leader in managing today’s increased compliance</li>
    </ul>
  </section>

  <section class="column col-mission">
    <h2>Our Mission</h2>
    <p>Our customer service mission is to develop superior client relationships built on a mutual trust and a strategic partnership. This partnership is built through our superior industry knowledge, clear understanding of client objectives and expectations, and from the extraordinary value K&amp;V provides beyond the programs we deliver. Our excellence is defined by unwavering quality of work, attention to detail, consistent/timely communications, flexibility to change, and through fair and reasonable pricing. Ultimately, it is our commitment to these values that result in anticipating and exceeding our clients expectations.</p>
  </section>

  <section class="news">
    <h2>News</h2>
    <ul>
      <li><time>2012.05.22</time><a href="#">A full service medical education agency</a></li>
      <li><time>2012.04.21</time><a href="#">Going beyond the program… Delivering solutions.</a></li>
      <li><time>2012.10.03</time><a href="#">Goin Understanding your strategic issues.</a></li>
      <li><time>2012.11.07</time><a href="#">Customer Service Oriented Compliance Leadership.</a></li>
      <li><time>2012.10.10</time><a href="#">Customer Service Oriented Compliance Leadership.</a></li>
      <li><time>2012.12.05</time><a href="#">A full service medical education agency that goes beyond the expected.</a></li>
    </ul>
  </section>

  <footer class="site-footer">
    <p>418 Harlow Pine Ave, Suite 200, Westmere, FL 34590 (<a href="#">view on map</a>) &nbsp;|&nbsp; P: 555.014.2730 &nbsp;|&nbsp; F: 555.014.2788</p>
    <p><small>Copyright (c) 2012 K&amp;V Medlink Communications | Privacy Statement | Terms Of Use</small></p>
  </footer>
</body>
</html>
```